Start-up lawncare company needing marketing flyer to promote business model

Hello! We are looking for a marketing flyer design with the requirements below.

We would like the size to fit a flyer that is 6.25" X 9", Front and Back.

We need these to meet the KBMR ORTQ requirements, there are details attached for the indicias that need to be included, and where to put them on the back of the flyer.

Here's the items items we would like to have included on the flyer:
- Logo (Attached)

- I attached a snip of how our website looks, as well as how our app looks, and would like to follow that general color scheme

- References to our Fernquill App, in both Zenthra and Vorby stores, and our website (www.Fernquill.com)

- Reference to the neighborhood barometer and gets the point across that the more of their neighbors that sign up, the cheaper the price of service (Visual attached of what this barometer looks like)

- We are licensed and insured landscaping pros

- Real, instant, upfront pricing for mowing, mulching and most other services

- Sign up with a few easy steps and manage your account from our app or online

- Automated safe & secure transactions upon service completion and satisfaction

- Excellent customer service with our quality guaranteed commitment!

- Sign up now and receive 50% off your first mow!

- Veteran owned

- A portion of our proceeds go to "Rennick Dolby Foundation"

- List's out all of the services we will offer
- Mowing
- Mulching
- Aeration and Over-seeding
- Fertilization
- Shrub/Tree Trimming
- Leaf removal and yard clean up
- Accent lighting installation
- Sprinkler blow-out / Winterization
- Driveway pressure washing and sealing
- Firewood Delivery

Target Market(s)

Homeowners in large neighborhoods that need lawn care services

Industry/Entity Type

Lawn Care

Font styles to use
Sans Serif

Colors

Designer to choose colors to be used in the design.

Requirements
Must have
• Meet KBMR ORTQ requirements
• Keep a similar color scheme to our website, feel free to use bold accents to make it more eye-catching as people search through their mail
• Get the general point across that as more of their neighbors sign up with us, the cheaper their service will be

```html
<!DOCTYPE html>
<html lang="en">
<head>
<meta charset="utf-8">
<title>Fernquill Flyer – Front and Back</title>
<link rel="stylesheet" href="https://fonts.googleapis.com/css2?family=Montserrat:wght@800;900&family=Roboto:wght@400;500;700;900&family=Roboto+Condensed:wght@400;500&display=swap">
<style>
  :root {
    --page-bg: #e4e4e4;
    --grass-light: #7cc242;
    --grass-mid: #3f9a2c;
    --grass-dark: #1f6e22;
    --teal: #13a89e;
    --green-brand: #2e9a3c;
    --yellow: #f5d90a;
    --ink: #1b1b1b;
    --white: #ffffff;
    --frame-grey: #c9c9c9;
  }
  * { box-sizing: border-box; margin: 0; padding: 0; }
  html, body { width: 928px; height: 1200px; overflow: hidden; }
  body { background: var(--page-bg); position: relative; font-family: "Roboto", Arial, sans-serif; }

  .flyer { position: absolute; left: 40px; width: 848px; height: 548px; overflow: hidden; background: var(--white); box-shadow: 0 6px 18px rgba(0,0,0,.18); }
  .flyer--front { top: 36px; }
  .flyer--back { top: 616px; }

  /* FRONT */
  .front-grass { position: absolute; inset: 0; background: linear-gradient(160deg, var(--grass-light) 0%, var(--grass-mid) 45%, var(--grass-dark) 100%); }
  .front-shapes { position: absolute; inset: 0; }
  .mower-photo { position: absolute; left: 392px; top: 22px; width: 190px; height: 285px; border-radius: 18px; background: linear-gradient(180deg, #2b2b2b 0%, #3a3a3a 45%, #d9282f 70%, #b51d24 100%); opacity: .9; }
  .headline { position: absolute; left: 40px; top: 38px; font-family: "Montserrat", Arial, sans-serif; font-weight: 900; font-size: 25px; line-height: 1.14; color: var(--white); text-transform: uppercase; text-shadow: 0 1px 3px rgba(0,0,0,.25); }
  .headline .accent { color: var(--yellow); }
  .intro { position: absolute; left: 42px; top: 176px; width: 255px; font-size: 13.5px; line-height: 1.3; color: var(--white); }
  .brand-front { position: absolute; left: 612px; top: 78px; display: flex; align-items: center; gap: 10px; font-weight: 900; font-size: 36px; color: var(--white); }
  .brand-dot { width: 18px; height: 18px; border-radius: 50%; background: var(--yellow); }
  .circle-photo { position: absolute; border-radius: 50%; border: 7px solid var(--white); box-shadow: -4px 0 0 var(--frame-grey); }
  .circle-photo--house { left: 655px; top: 135px; width: 240px; height: 240px; background: radial-gradient(circle at 60% 25%, #e9e2d2 0%, #c9c1ad 30%, #6fae3a 55%, #4f9a2a 100%); }
  .circle-photo--path { left: 598px; top: 330px; width: 200px; height: 200px; background: radial-gradient(circle at 55% 55%, #bdbdbd 0%, #9aa28f 22%, #6db33f 50%, #3f8a2a 100%); }
  .benefits { position: absolute; left: 48px; top: 344px; list-style: none; font-family: "Roboto Condensed", Arial, sans-serif; font-size: 14px; line-height: 19px; color: var(--ink); }
  .benefits li { display: flex; align-items: center; gap: 8px; }
  .tick { width: 11px; height: 11px; flex: none; }

  /* BACK */
  .back-wash { position: absolute; left: 0; top: 0; width: 520px; height: 260px; background: linear-gradient(180deg, var(--teal) 0%, #52c3ad 40%, rgba(255,255,255,0) 100%); }
  .back-shapes { position: absolute; inset: 0; }
  .brand-back { position: absolute; left: 47px; top: 78px; display: flex; align-items: center; gap: 10px; font-weight: 900; font-size: 40px; color: var(--white); }
  .brand-back .brand-dot { background: var(--white); }
  .services-title { position: absolute; left: 47px; top: 208px; font-size: 21px; font-weight: 700; color: var(--green-brand); }
  .services { position: absolute; left: 47px; top: 244px; list-style: none; font-size: 16px; font-weight: 500; line-height: 21.5px; color: var(--ink); }
  .services li { display: flex; align-items: center; gap: 9px; }
  .services .tick { width: 13px; height: 13px; }
  .contact { position: absolute; left: 47px; top: 500px; color: var(--white); font-size: 14px; line-height: 22px; }
  .contact .phone { font-family: "Montserrat", Arial, sans-serif; font-weight: 800; font-size: 15px; letter-spacing: .5px; }
</style>
</head>
<body>

<section class="flyer flyer--front" aria-label="Flyer front">
  <div class="front-grass" role="img" aria-label="Photo of a freshly mown green lawn field"></div>
  <div class="mower-photo" role="img" aria-label="Photo of a red and black push lawn mower"></div>

  <svg class="front-shapes" viewBox="0 0 848 548" width="848" height="548" aria-hidden="true">
    <path d="M330,300 C450,270 560,245 700,205 L705,214 C565,256 455,282 335,308 Z" fill="var(--yellow)"/>
    <path d="M0,332 C200,318 420,285 700,214 L848,180 L848,548 L0,548 Z" fill="var(--white)"/>
    <path d="M0,532 C250,522 480,504 640,478 L848,430 L848,548 L0,548 Z" fill="var(--teal)"/>
  </svg>

  <h1 class="headline"><span class="accent">Your Landscaping</span><br>Service Needs<br>Right to Your<br>Fingertips</h1>
  <p class="intro">We pair our local team with you and your neighbors utilizing our proven technology. Which by the way, saves you time and money!</p>

  <div class="brand-front"><span class="brand-dot"></span>Fernquill</div>

  <div class="circle-photo circle-photo--house" role="img" aria-label="Photo of a house porch with flower beds and green lawn"></div>
  <div class="circle-photo circle-photo--path" role="img" aria-label="Photo of a curving stone garden path through a lawn"></div>

  <ul class="benefits">
    <li><svg class="tick" viewBox="0 0 12 12"><path d="M1,6 L4.5,10 L11,1.5" fill="none" stroke="var(--green-brand)" stroke-width="2"/></svg>We are licensed and insured landscaping pros</li>
    <li><svg class="tick" viewBox="0 0 12 12"><path d="M1,6 L4.5,10 L11,1.5" fill="none" stroke="var(--green-brand)" stroke-width="2"/></svg>Real, instant, upfront pricing for mowing, mulching and most other services</li>
    <li><svg class="tick" viewBox="0 0 12 12"><path d="M1,6 L4.5,10 L11,1.5" fill="none" stroke="var(--green-brand)" stroke-width="2"/></svg>Sign up with a few easy steps and manage your account from our app or online</li>
    <li><svg class="tick" viewBox="0 0 12 12"><path d="M1,6 L4.5,10 L11,1.5" fill="none" stroke="var(--green-brand)" stroke-width="2"/></svg>Automated safe &amp; secure transactions upon service completion and satisfaction</li>
    <li><svg class="tick" viewBox="0 0 12 12"><path d="M1,6 L4.5,10 L11,1.5" fill="none" stroke="var(--green-brand)" stroke-width="2"/></svg>Excellent customer service with our quality guaranteed commitment!</li>
    <li><svg class="tick" viewBox="0 0 12 12"><path d="M1,6 L4.5,10 L11,1.5" fill="none" stroke="var(--green-brand)" stroke-width="2"/></svg>Sign up now and receive 50% off your first mow!</li>
    <li><svg class="tick" viewBox="0 0 12 12"><path d="M1,6 L4.5,10 L11,1.5" fill="none" stroke="var(--green-brand)" stroke-width="2"/></svg>Veteran owned</li>
    <li><svg class="tick" viewBox="0 0 12 12"><path d="M1,6 L4.5,10 L11,1.5" fill="none" stroke="var(--green-brand)" stroke-width="2"/></svg>A portion of our proceeds go to “Rennick Dolby Foundation”</li>
  </ul>
</section>

<section class="flyer flyer--back" aria-label="Flyer back">
  <div class="back-wash"></div>
  <svg class="back-shapes" viewBox="0 0 848 548" width="848" height="548">
    <defs>
      <linearGradient id="parkTones" x1="0" y1="0" x2="0" y2="1">
        <stop offset="0" stop-color="#a9c94a"/>
        <stop offset=".45" stop-color="#4f7d2a"/>
        <stop offset=".7" stop-color="#e0502a"/>
        <stop offset=".85" stop-color="#7ac043"/>
        <stop offset="1" stop-color="#9fd35a"/>
      </linearGradient>
    </defs>
    <path d="M0,486 L500,486 C495,515 470,535 445,548 L0,548 Z" fill="var(--teal)"/>
    <path d="M278,0 C380,40 420,110 380,170 C330,230 300,280 360,360 C420,430 520,460 500,500 C490,525 470,538 445,548 L848,548 L848,0 Z" fill="var(--white)"/>
    <path d="M290,0 C392,40 432,110 392,170 C342,230 312,280 372,360 C432,430 532,460 512,500 C502,525 482,538 457,548 L848,548 L848,0 Z" fill="url(#parkTones)" role="img" aria-label="Photo of a man driving an orange ride-on mower on a sunny lawn under trees"/>
  </svg>

  <div class="brand-back"><span class="brand-dot"></span>Fernquill</div>

  <h2 class="services-title">Services</h2>
  <ul class="services">
    <li><svg class="tick" viewBox="0 0 12 12"><path d="M1,6 L4.5,10 L11,1.5" fill="none" stroke="var(--green-brand)" stroke-width="2"/></svg>Mowing</li>
    <li><svg class="tick" viewBox="0 0 12 12"><path d="M1,6 L4.5,10 L11,1.5" fill="none" stroke="var(--green-brand)" stroke-width="2"/></svg>Mulching</li>
    <li><svg class="tick" viewBox="0 0 12 12"><path d="M1,6 L4.5,10 L11,1.5" fill="none" stroke="var(--green-brand)" stroke-width="2"/></svg>Aeration and Over-seeding</li>
    <li><svg class="tick" viewBox="0 0 12 12"><path d="M1,6 L4.5,10 L11,1.5" fill="none" stroke="var(--green-brand)" stroke-width="2"/></svg>Fertilization</li>
    <li><svg class="tick" viewBox="0 0 12 12"><path d="M1,6 L4.5,10 L11,1.5" fill="none" stroke="var(--green-brand)" stroke-width="2"/></svg>Shrub/Tree Trimming</li>
    <li><svg class="tick" viewBox="0 0 12 12"><path d="M1,6 L4.5,10 L11,1.5" fill="none" stroke="var(--green-brand)" stroke-width="2"/></svg>Leaf removal and yard clean up</li>
    <li><svg class="tick" viewBox="0 0 12 12"><path d="M1,6 L4.5,10 L11,1.5" fill="none" stroke="var(--green-brand)" stroke-width="2"/></svg>Accent lighting installation</li>
    <li><svg class="tick" viewBox="0 0 12 12"><path d="M1,6 L4.5,10 L11,1.5" fill="none" stroke="var(--green-brand)" stroke-width="2"/></svg>Sprinkler blow-out / Winterization</li>
    <li><svg class="tick" viewBox="0 0 12 12"><path d="M1,6 L4.5,10 L11,1.5" fill="none" stroke="var(--green-brand)" stroke-width="2"/></svg>Driveway pressure washing and sealing</li>
    <li><svg class="tick" viewBox="0 0 12 12"><path d="M1,6 L4.5,10 L11,1.5" fill="none" stroke="var(--green-brand)" stroke-width="2"/></svg>Firewood Delivery</li>
  </ul>

  <div class="contact">
    <div>Your location, Street, Post Code</div>
    <div><span class="phone">555-014-2290</span> | www.Fernquill.com</div>
  </div>
</section>

</body>
</html>
```